Business Card Design Project

Corvexa logo will be provided after
Front

Bram Oskarsen- Construction Manager

Ph: (61) 07 53182907
boskarsen@corvexa.com.au
PO Box 83 Kelbarra 4529

Back
Corvexa
EPCM

Oil - Gas - Mining

Industry/Entity Type

Business

Font styles to use
Sans Serif

Colors
faa54b

Requirements
Must have
• White Back Ground

```html
<!DOCTYPE html>
<html lang="en">
<head>
<meta charset="utf-8">
<title>Corvexa – Business Card</title>
<link rel="stylesheet" href="https://fonts.googleapis.com/css2?family=Open+Sans:wght@400;600;700;800&display=swap">
<style>
  :root {
    --orange: #f39121;
    --orange-back: #f0932a;
    --ink: #141414;
    --text: #3a3a3a;
    --paper: #ffffff;
    --stage: #ffffff;
    --edge: #4a4a4a;
  }
  * { margin: 0; padding: 0; box-sizing: border-box; }
  html, body {
    width: 1136px; height: 1200px; overflow: hidden;
    background: var(--stage);
    font-family: "Open Sans", Arial, sans-serif;
  }
  .sheet { position: relative; width: 1136px; height: 1200px; }

  .card {
    position: absolute; width: 847px; height: 485px;
    border: 1px solid var(--edge);
    overflow: hidden;
  }

  /* Front */
  .card--front { left: 197px; top: 101px; background: var(--paper); }
  .front__band {
    position: absolute; left: 0; top: 0; width: 130px; height: 100%;
    background: var(--orange);
  }
  .front__rule {
    position: absolute; left: 132px; top: 0; width: 4px; height: 100%;
    background: var(--ink);
  }
  .front__wordmark {
    position: absolute; left: 150px; top: 90px;
    font-weight: 800; font-size: 94px; letter-spacing: 16px;
    color: var(--ink); line-height: 1; text-transform: uppercase;
    white-space: nowrap;
  }
  .contact { position: absolute; left: 170px; top: 286px; list-style: none; }
  .contact__item {
    display: flex; align-items: center; gap: 11px;
    height: 27.5px; font-size: 21px; color: var(--text); white-space: nowrap;
  }
  .contact__icon { width: 20px; height: 20px; flex: none; }
  .front__address {
    position: absolute; left: 170px; top: 390px;
    font-size: 21px; line-height: 29px; color: var(--text); white-space: nowrap;
  }
  .person { position: absolute; right: 22px; top: 286px; text-align: right; white-space: nowrap; }
  .person__name { font-weight: 700; font-size: 24px; line-height: 34px; color: var(--orange); }
  .person__role { font-size: 21px; line-height: 32px; color: var(--ink); }

  /* Back */
  .card--back { left: 93px; top: 614px; background: var(--orange-back); }
  .back__wordmark {
    position: absolute; left: 0; right: 0; top: 167px; text-align: center;
    font-weight: 800; font-size: 97px; letter-spacing: 22px; padding-left: 22px;
    color: var(--paper); line-height: 1; text-transform: uppercase;
    white-space: nowrap;
  }
  .back__web {
    position: absolute; left: 0; right: 0; top: 332px; text-align: center;
    font-size: 25px; line-height: 34px; letter-spacing: 6px; padding-left: 6px;
    color: var(--paper);
  }
  .back__sector {
    position: absolute; left: 0; right: 0; top: 404px; text-align: center;
    font-size: 18px; font-weight: 600; line-height: 26px; letter-spacing: 3px;
    padding-left: 3px; color: var(--paper);
  }
</style>
</head>
<body>
<main class="sheet">
  <section class="card card--front" aria-label="Card front">
    <div class="front__band"></div>
    <div class="front__rule"></div>
    <div class="front__wordmark">Corvexa</div>

    <ul class="contact">
      <li class="contact__item">
        <svg class="contact__icon" viewBox="0 0 20 20" aria-hidden="true">
          <circle cx="10" cy="10" r="8.5" fill="none" stroke="var(--orange)" stroke-width="1.3"/>
          <path d="M7 5.5c-1 .8-1.2 2.2-.4 4l1.2 2.2c1 1.6 2.2 2.6 3.5 2.6l1-.9-1.6-2-1 .4-1.5-2.6.8-.7L8 5.2z" fill="var(--orange)"/>
        </svg>
        <span>(61) 07 53182907</span>
      </li>
      <li class="contact__item">
        <svg class="contact__icon" viewBox="0 0 20 20" aria-hidden="true">
          <rect x="1.5" y="5" width="17" height="12" fill="var(--orange)"/>
          <polyline points="1.5,5 10,11.5 18.5,5" fill="none" stroke="#fff" stroke-width="1.4"/>
        </svg>
        <span>boskarsen@corvexa.com.au</span>
      </li>
      <li class="contact__item">
        <svg class="contact__icon" viewBox="0 0 20 20" aria-hidden="true">
          <g fill="none" stroke="var(--orange)" stroke-width="1.3">
            <circle cx="10" cy="10" r="8.5"/>
            <ellipse cx="10" cy="10" rx="3.8" ry="8.5"/>
            <line x1="1.5" y1="10" x2="18.5" y2="10"/>
            <line x1="3" y1="5.5" x2="17" y2="5.5"/>
            <line x1="3" y1="14.5" x2="17" y2="14.5"/>
          </g>
        </svg>
        <span>www.corvexa.com.au</span>
      </li>
    </ul>

    <p class="front__address">PO Box 83 Kelbarra 4529</p>

    <div class="person">
      <p class="person__name">Bram Oskarsen</p>
      <p class="person__role">Construction Manager</p>
    </div>
  </section>

  <section class="card card--back" aria-label="Card back">
    <div class="back__wordmark">Corvexa</div>
    <p class="back__web">www.corvexa.com.au</p>
    <p class="back__sector">EPCM &nbsp;|&nbsp; Oil - Gas - Mining</p>
  </section>
</main>
</body>
</html>
```